Audit/Compliance company needs Business Card Template

We are after a Business Card Template that we can modify internally to update details as people change positions.
We are an Australian based company specalising in Auditing and Quality/OHS systems development. - See www.keelbrookmeridian.com.au for more information
We would like the desings to be based around our logo and colours assocaited with it (attached for your information) however we are very open as to how the cards are designed.
We are looking for something quite edgy and mordern but it must have a professional/compliance feel to it (if possible).
The main details we would like to include within the card template are:
Name
Position Title
Postal Address
Phone Number
Mobile Number
Email Address
Website
The cards will be printed through folio mint on Glossy paper so it should reflect the requirements below
Full Bleed Size (starting document size)
90 x 52 mm
1062 x 615 pixels
Document Trim Size (final size after being cut)
87 x 49 mm
1028 x 579 pixels
Resolution
300 DPI

```html
<!DOCTYPE html>
<html lang="en">
<head>
<meta charset="utf-8">
<title>Keelbrook Meridian – Business Card</title>
<link rel="stylesheet" href="https://fonts.googleapis.com/css2?family=Cabin:wght@400;500&display=swap">
<style>
  :root {
    --page: #ffffff;
    --navy-top: #121e33;
    --navy-bottom: #0c1628;
    --brand-orange: #f08a1c;
    --brand-orange-faint: #f8d3ad;
    --brand-blue: #2e6f9e;
    --brand-blue-faint: #c3ced8;
    --name-grey: #8a8f98;
    --title-grey: #767c86;
    --text-grey: #6a6a6a;
    --frame: #333333;
    --body-font: "Cabin", "Candara", sans-serif;
  }
  * { box-sizing: border-box; margin: 0; padding: 0; }
  html, body {
    width: 1128px; height: 1200px; overflow: hidden;
    background: var(--page);
    font-family: var(--body-font);
  }
  .canvas { position: relative; width: 1128px; height: 1200px; }

  .card { position: absolute; left: 100px; width: 936px; height: 534px; }
  .card--front {
    top: 39px;
    background: linear-gradient(180deg, var(--navy-top), var(--navy-bottom));
  }
  .card--back {
    top: 619px;
    background: var(--page);
    border: 1px solid var(--frame);
  }

  .brand {
    position: absolute; left: 0; right: 0;
    display: flex; align-items: center; justify-content: center; gap: 18px;
  }
  .brand__mark { width: 34px; height: 34px; border-radius: 50%; background: var(--brand-blue); }
  .brand__name {
    font-size: 30px; font-weight: 500; letter-spacing: 0.5px;
    color: var(--brand-orange); text-transform: uppercase;
  }
  .card--front .brand { top: 166px; }
  .card--back .brand { top: 98px; }
  .card--back .brand__mark { background: var(--brand-blue-faint); }
  .card--back .brand__name { color: var(--brand-orange-faint); }

  .holder { position: absolute; top: 316px; left: 0; right: 0; text-align: center; }
  .holder__name { font-size: 31px; color: var(--name-grey); line-height: 1.2; }
  .holder__role { font-size: 22px; color: var(--title-grey); margin-top: 6px; }

  .contact {
    position: absolute; top: 181px; left: 0; right: 0;
    list-style: none; text-align: center;
    font-size: 24px; color: var(--text-grey);
  }
  .contact li { height: 55px; line-height: 30px; }
  .contact li:nth-child(n+3) { height: 59px; }
</style>
</head>
<body>
<main class="canvas">
  <section class="card card--front" aria-label="Card front">
    <div class="brand">
      <span class="brand__mark"></span>
      <span class="brand__name">Keelbrook Meridian</span>
    </div>
    <div class="holder">
      <p class="holder__name">Dara Whitlow</p>
      <p class="holder__role">Manager</p>
    </div>
  </section>

  <section class="card card--back" aria-label="Card back">
    <div class="brand">
      <span class="brand__mark"></span>
      <span class="brand__name">Keelbrook Meridian</span>
    </div>
    <ul class="contact">
      <li>123456789</li>
      <li>Phone number</li>
      <li>email@email.com</li>
      <li>www.keelbrookmeridian.com.au</li>
      <li>Unit 123, Harbour Row, Sydney, Australia</li>
    </ul>
  </section>
</main>
</body>
</html>
```